UK based media owner TALVEX (http://www.talvex.uk/) needs DIGITAL ADVERT to run on our digital panel

Hi guys,

Thanks for taking the time to have a look at this brief.
I need someone to create a digital advert (still/static design or video) to run on our digital panels which are located across UK university student unions.
For who wants to upload a video ---> All of our panels are digitally enabled and allow for full motion video – they run adverts 10 seconds long (see artwork specification document in attachment) therefore the advert will have to be 10 seconds long.
For static/still design ----> see artwork specification to see resolution etc

I need something professional looking, polished yet fresh and exciting so that it speaks and connects to this younger audience – we want to inspire them to take a step towards new levels of business opportunities.

Here are some Key Points you’ll need to take into consideration when designing the advert:

Overall Campaign Objective: To excite and attract young entrepreneurs to get in touch with us for possible partnerships

Target Audience: Young entrepreneurs attending university (university students – 18 to 24 years old)

Creative Specifications: See attached document with artwork specifications

Text on Advert:

I need the following text to appear on the advert: (Please include company logo)

“Do you have a business idea that would benefit with advertising on these screens?

We want to support young entrepreneurs and will partner with any whom have a great idea

WE WANT TO HEAR FROM YOU!

Email us at ideas@talvex.uk
www.talvex.uk/ideas”

I would need some ideas by the 3rd July 2018 if possible.

Thanks to all who will take part in this project – contact me if you have any questions

Target Market(s)

Young entrepreneurs attending university (university students – 18 to 24 years old)

Requirements
Must have
• I need the following text to appear on the advert: (Please include company logo)
• “Do you have a business idea that would benefit with advertising on these screens?
• We want to support young entrepreneurs and will partner with any whom have a great idea
• WE WANT TO HEAR FROM YOU!
• Email us at ideas@talvex.uk
• www.talvex.uk/ideas”

```html
<!DOCTYPE html>
<html lang="en">
<head>
<meta charset="utf-8">
<title>TALVEX – We Want To Hear From You</title>
<link href="https://fonts.googleapis.com/css2?family=Montserrat:wght@400;500;800;900&display=swap" rel="stylesheet">
<style>
  :root {
    --page-bg: #ededed;
    --red-light: #a8252f;
    --red-mid: #8a1620;
    --red-dark: #5a0b12;
    --brand-red: #c91f2b;
    --contact-red: #8e1a24;
    --white: #ffffff;
  }
  * { margin: 0; padding: 0; box-sizing: border-box; }
  html, body {
    width: 1200px; height: 942px; overflow: hidden;
    background: var(--page-bg);
    font-family: "Montserrat", Arial, sans-serif;
  }
  .advert {
    position: absolute; left: 350px; top: 32px;
    width: 500px; height: 878px;
    background: var(--white);
    box-shadow: 0 4px 14px rgba(0,0,0,0.18);
    overflow: hidden;
  }
  .advert__backdrop { position: absolute; left: 0; top: 0; width: 500px; height: 610px; }
  .advert__text { position: absolute; left: 0; width: 100%; text-align: center; color: var(--white); white-space: nowrap; }
  .question { top: 22px; font-size: 21px; font-weight: 500; line-height: 29px; letter-spacing: 0.2px; }
  .question__screens { top: 82px; font-size: 44px; font-weight: 900; line-height: 50px; letter-spacing: -0.5px; }
  .support { top: 166px; font-size: 20px; font-weight: 500; line-height: 24px; }
  .headline { font-weight: 900; letter-spacing: -3px; line-height: 1; }
  .headline--we { top: 284px; font-size: 88px; }
  .headline--hear { top: 361px; font-size: 88px; }
  .headline--from {
    top: 436px; left: 28px; width: auto; text-align: left;
    font-size: 34px; font-weight: 500; letter-spacing: -0.5px;
  }
  .headline--you { top: 430px; left: 172px; width: auto; text-align: left; font-size: 120px; letter-spacing: -5px; }
  .brand {
    position: absolute; top: 668px; left: 0; width: 100%;
    display: flex; justify-content: center; align-items: center; gap: 14px;
    color: var(--brand-red); font-size: 54px; font-weight: 800; letter-spacing: -1px;
  }
  .brand__dot { width: 26px; height: 26px; border-radius: 50%; background: var(--brand-red); }
  .contact {
    position: absolute; left: 0; width: 100%;
    display: flex; justify-content: center; align-items: center; gap: 10px;
    color: var(--contact-red); font-size: 27px; font-weight: 800; letter-spacing: -0.3px;
    white-space: nowrap;
  }
  .contact--email { top: 788px; }
  .contact--web { top: 826px; }
  .contact__icon { width: 26px; height: 26px; flex: none; }
</style>
</head>
<body>
  <main class="advert">
    <svg class="advert__backdrop" viewBox="0 0 500 610" aria-hidden="true">
      <defs>
        <radialGradient id="redGlow" cx="0.35" cy="0.35" r="0.8">
          <stop offset="0" stop-color="var(--red-light)"/>
          <stop offset="0.6" stop-color="var(--red-mid)"/>
          <stop offset="1" stop-color="var(--red-dark)"/>
        </radialGradient>
      </defs>
      <path d="M0 0 H500 V545 Q250 655 0 545 Z" fill="url(#redGlow)"/>
    </svg>

    <p class="advert__text question">Do you have a business idea that<br>would benefit with advertising on</p>
    <p class="advert__text question__screens">THESE SCREENS?</p>
    <p class="advert__text support">We want to support young<br>entrepreneurs and will partner with<br>any whom have a great idea</p>

    <h1>
      <span class="advert__text headline headline--we">WE WANT</span>
      <span class="advert__text headline headline--hear">TO HEAR</span>
      <span class="advert__text headline headline--from">FROM</span>
      <span class="advert__text headline headline--you">YOU!</span>
    </h1>

    <div class="brand">
      <span class="brand__dot"></span>
      <span class="brand__name">talvex</span>
    </div>

    <p class="contact contact--email">
      <svg class="contact__icon" viewBox="0 0 26 26" aria-hidden="true">
        <rect x="2" y="6" width="22" height="15" fill="none" stroke="currentColor" stroke-width="1.8"/>
        <path d="M2 6 L13 15 L24 6 M2 21 L10 13 M24 21 L16 13" fill="none" stroke="currentColor" stroke-width="1.8"/>
      </svg>
      IDEAS@TALVEX.UK
    </p>
    <p class="contact contact--web">
      <svg class="contact__icon" viewBox="0 0 26 26" aria-hidden="true">
        <g fill="none" stroke="currentColor" stroke-width="1.6">
          <circle cx="13" cy="13" r="10"/>
          <ellipse cx="13" cy="13" rx="4.5" ry="10"/>
          <path d="M3 13 H23 M5 7.5 H21 M5 18.5 H21"/>
        </g>
      </svg>
      WWW.TALVEX.UK/IDEAS
    </p>
  </main>
</body>
</html>
```